Tobias Wrenfield - Cinematographer

NEED:
I'm looking for a sleek, professional, modern business card that will give give the recipient the impression that they can trust their production will go smoothly by hiring me. I will bring creativity and knowledge to their shoot, so that we can create powerful images.
I am looking for a card with a strong style and design ethos that could be expanded to a website and a full visual/graphic/design entity for me.
ABOUT ME:
I am a mid-twenties cinematographer, I work on music video, narrative short, commercial, and corporate projects. I blend the science and artistry of cameras and filmmaking to tell a story. I'm an artist, a technician, and a manager.
DESIGN:
I like sleek, simple design. Black, dark grays, white, dark navy, steel blues, I love cyan, but also cyan and red. I am not a fan of earthy tones. I generally prefer modern, san-serif fonts over serifs. My old logo was based on an aperture, a multi-blade device at the back of a lens that controls how much light passes through, but I made it with so many colors, that it doesn't necessarily lend itself to a specific color-scheme or design ethos. I liked that the aperture design provided a sense of the technical requirements of my job. I'm a fan of matte business cards, but am open to plenty of specialty print processes to make an outstanding card.
ATTACHED FILES:
My Old Rainbox Aperture Logo, plus a few designs I've tried playing around with, but am not tied to. I AM OPEN TO NEW DESIGNS, DO NOT FEEL TIED TO THIS.
**I've pulled my old logo down from the attached files, and instead attached other business cards I like, so as not to mislead you where I would like to go.
INFO:
Name: Tobias Wrenfield
Job: Cinematographer
Email: tkwrenfield@quillbox.example
Phone: 503.618.2907
Website: tobiaswrenfield.example
Updates
I'm adding some images of other cards that I like, and removing my old logo, since I'm looking for something new, and don't want that old logo to push anyone a certain direction.

```html
<!DOCTYPE html>
<html lang="en">
<head>
<meta charset="utf-8">
<title>Tobias Wrenfield – Cinematographer Business Card</title>
<link rel="stylesheet" href="https://fonts.googleapis.com/css2?family=Arimo:wght@400;700&display=swap">
<style>
  :root {
    --card-black: #000000;
    --ink-white: #ffffff;
    --rule-grey: #cfcfcf;
    --accent-yellow: #f2e600;
    --mark-cyan: #18a9e0;
  }
  html, body {
    margin: 0;
    padding: 0;
    width: 887px;
    height: 1200px;
    overflow: hidden;
    background: var(--card-black);
  }
  .card-sheet {
    display: block;
    width: 887px;
    height: 1200px;
    font-family: "Arimo", Arial, sans-serif;
  }
  .name-word { fill: var(--ink-white); font-weight: 700; }
  .role-word { fill: var(--ink-white); font-weight: 400; }
  .accent-rule { stroke: var(--accent-yellow); stroke-width: 2; }
  .crosshair-rule { stroke: var(--rule-grey); stroke-width: 1.5; }
  .contact-email { fill: var(--ink-white); font-size: 24px; font-weight: 400; letter-spacing: 0.5px; }
  .contact-phone { fill: var(--ink-white); font-size: 24px; font-weight: 700; letter-spacing: 1px; }
  .contact-web { fill: var(--ink-white); font-size: 25px; font-weight: 700; letter-spacing: 1.5px; }
  .brand-dot { fill: var(--mark-cyan); }
</style>
</head>
<body>
<svg class="card-sheet" viewBox="0 0 887 1200" xmlns="http://www.w3.org/2000/svg">
  <defs>
    <linearGradient id="divider-glow" x1="0" x2="1" y1="0" y2="0">
      <stop offset="0" stop-color="#ffffff"/>
      <stop offset="0.38" stop-color="#ffffff"/>
      <stop offset="0.56" stop-color="#fff200"/>
      <stop offset="0.66" stop-color="#ffffff"/>
      <stop offset="0.86" stop-color="#fff200"/>
      <stop offset="1" stop-color="#ffffff"/>
    </linearGradient>
  </defs>

  <rect width="887" height="1200" fill="var(--card-black)"/>

  <!-- Back face: header lockup -->
  <g class="header-lockup">
    <circle class="brand-dot" cx="92" cy="92" r="54"/>
    <text class="name-word" x="154" y="94" font-size="48" textLength="434" lengthAdjust="spacing">TOBIAS WRENFIELD</text>
    <line class="accent-rule" x1="154" y1="97" x2="588" y2="97"/>
    <text class="role-word" x="154" y="127" font-size="34" textLength="434" lengthAdjust="spacing">CINEMATOGRAPHER</text>
  </g>

  <!-- Back face: contact block -->
  <g class="contact-block">
    <line class="crosshair-rule" x1="40" y1="423" x2="854" y2="423"/>
    <line class="crosshair-rule" x1="487" y1="374" x2="487" y2="494"/>
    <text class="contact-email" x="496" y="453">tkwrenfield@quillbox.example</text>
    <text class="contact-phone" x="496" y="493">503.618.2907</text>
    <text class="contact-web" x="854" y="554" text-anchor="end">www.tobiaswrenfield.example</text>
  </g>

  <!-- Divider between card faces -->
  <rect class="face-divider" x="0" y="592" width="887" height="16" fill="url(#divider-glow)"/>

  <!-- Front face: centred lockup -->
  <g class="front-lockup">
    <circle class="brand-dot" cx="446" cy="816" r="94"/>
    <text class="name-word" x="154" y="997" font-size="56" textLength="578" lengthAdjust="spacing">TOBIAS WRENFIELD</text>
    <line class="accent-rule" x1="154" y1="1001" x2="732" y2="1001"/>
    <text class="role-word" x="154" y="1039" font-size="38" textLength="578" lengthAdjust="spacing">CINEMATOGRAPHER</text>
  </g>
</svg>
</body>
</html>
```